Flyer for annual KESTREL SUMMIT 2020

I would like a church event flyer designed. The event is called "KESTREL SUMMIT 2020". I am looking for a professional, yet catchy design that uses our brand colors and logo creatively while communicating key information of the event effectively.

1. The logo is attached in two color formats. The designer has the choice to use them as he/she want.

2. The location of the event is: Harlow Community Center, 239 Fennimore Street, Portland, ME 04117

3. Time and date of event. The designer can organize and format the date and time as he/she pleases.
Thursday December 31st @ 6:30PM
Friday January 1st @ 6:30PM
Saturday 2nd @ 6:30PM
Sunday 3rd @ 4:30PM

4. The topic of the event is "In Fire and On Fire". The designer is free to use this phrase as he/she pleases to create a good composition.

5. Speaker: Prophet Marcus Olunde (2 pictures of the speaker to choose from are attached)

6. Contact information: contact@brightmeadowfold.org - Telephone number: 207 583 2914

7. I would also like the following three words on the flyer. These words describe the focus of the event: FIRE, REVIVAL, PROPHETIC

Target Market(s)

Young adults

Font styles to use
Sans Serif

Requirements
Must have
• Logo, speaker's picture
Should not have
• cross image, church image

```html
<!DOCTYPE html>
<html lang="en">
<head>
<meta charset="UTF-8">
<title>Kestrel Summit 2020 Flyer</title>
<link rel="stylesheet" href="https://fonts.googleapis.com/css2?family=Jost:wght@400&family=Montserrat:ital,wght@0,400;0,500;0,600;0,700;1,700&family=Oswald:wght@300;600&display=swap">
<style>
  :root {
    --navy: #0f2e4f;
    --navy-deep: #0b2440;
    --orange: #f39a21;
    --peach: #fde2c4;
    --white: #ffffff;
    --stage: #8c8c8c;
    --pin: #e3262d;
  }
  * { margin: 0; padding: 0; box-sizing: border-box; }
  html, body { width: 1200px; height: 1200px; overflow: hidden; background: var(--stage); }
  .flyer {
    position: absolute; left: 136px; top: 0;
    width: 928px; height: 1200px; overflow: hidden;
    background: var(--white);
    font-family: "Montserrat", Arial, sans-serif; color: var(--navy);
  }
  .flyer-backdrop { position: absolute; inset: 0; }
  .abs { position: absolute; white-space: nowrap; }
  h1 { font-weight: 400; }

  .brand-name { left: 624px; top: 116px; font-family: "Montserrat", sans-serif; font-weight: 600; font-size: 50px; line-height: 1; letter-spacing: 1px; color: var(--white); }

  .theme-note {
    position: absolute; left: 540px; top: 238px; width: 274px; height: 262px;
    background: var(--white); transform: rotate(-8deg);
    box-shadow: 0 6px 14px rgba(0,0,0,.25);
  }
  .theme-line { position: absolute; left: 0; width: 100%; text-align: center; font-family: "Oswald", sans-serif; font-weight: 600; font-size: 78px; line-height: 1; color: var(--navy-deep); transform: scaleX(.86); }
  .theme-line.first { top: 34px; }
  .theme-line.last { top: 160px; }
  .theme-band { position: absolute; left: 58px; top: 120px; width: 180px; height: 44px; background: var(--orange); color: var(--white); font-family: "Oswald", sans-serif; font-weight: 300; font-size: 36px; letter-spacing: 12px; text-align: center; line-height: 44px; padding-left: 10px; }
  .theme-pin { position: absolute; left: 128px; top: -18px; width: 26px; height: 26px; border-radius: 50%; background: var(--pin); }

  .title-top { left: 54px; top: 112px; font-family: "Jost", sans-serif; font-weight: 400; font-size: 96px; line-height: 1; color: var(--orange); letter-spacing: -2px; }
  .title-main { left: 52px; top: 196px; font-family: "Oswald", sans-serif; font-weight: 600; font-size: 110px; line-height: 1; color: var(--navy); letter-spacing: -1px; }
  .title-year { left: 54px; top: 300px; font-family: "Jost", sans-serif; font-weight: 400; font-size: 80px; line-height: 1; color: var(--orange); }
  .focus-words { left: 56px; top: 374px; font-style: italic; font-weight: 700; font-size: 28px; }

  .session { position: absolute; width: 200px; }
  .time-tag { position: relative; width: 128px; height: 72px; background: var(--white); clip-path: polygon(0 0, 100% 0, 92% 50%, 100% 100%, 0 100%); color: var(--orange); font-weight: 700; }
  .time-hour { position: absolute; left: 6px; top: 0; font-size: 64px; line-height: 72px; }
  .time-min { position: absolute; left: 50px; top: 6px; font-size: 38px; line-height: 1; }
  .time-pm { position: absolute; left: 66px; top: 42px; font-size: 22px; line-height: 1; }
  .session-day { margin-top: 12px; font-weight: 700; font-size: 22px; line-height: 26px; }
  .session-date { font-weight: 400; font-size: 21px; line-height: 27px; }

  .venue-name { left: 55px; top: 770px; font-weight: 600; font-size: 30px; }
  .venue-address { left: 55px; top: 808px; font-size: 19px; }

  .speaker-label { left: 55px; top: 898px; font-weight: 700; font-size: 36px; color: var(--white); }
  .speaker-name { left: 55px; top: 962px; font-weight: 700; font-size: 36px; }

  .contact-heading { left: 55px; top: 1058px; font-weight: 500; font-size: 24px; color: var(--orange); }
  .contact-email { left: 55px; top: 1092px; font-size: 26px; }
  .contact-line { left: 55px; top: 1125px; font-size: 26px; }
  .contact-line strong { font-weight: 700; }
</style>
</head>
<body>
<main class="flyer">
  <svg class="flyer-backdrop" width="928" height="1200" viewBox="0 0 928 1200">
    <defs>
      <linearGradient id="leftFade" x1="0" y1="0" x2="0" y2="1">
        <stop offset="0.38" stop-color="#ffffff"/>
        <stop offset="0.62" stop-color="#fde2c4"/>
        <stop offset="1" stop-color="#fde2c4"/>
      </linearGradient>
      <linearGradient id="heroTone" x1="0" y1="0" x2="1" y2="1">
        <stop offset="0" stop-color="#0f3a52"/>
        <stop offset="0.5" stop-color="#123a5c"/>
        <stop offset="1" stop-color="#0b2440"/>
      </linearGradient>
      <linearGradient id="speakerTone" x1="0" y1="0" x2="0" y2="1">
        <stop offset="0" stop-color="#3a2a22"/>
        <stop offset="0.35" stop-color="#d2502f"/>
        <stop offset="1" stop-color="#b8422a"/>
      </linearGradient>
    </defs>
    <rect width="928" height="1200" fill="url(#leftFade)"/>
    <path d="M0 1010 C250 1045 520 1030 640 1000 L640 1200 L0 1200 Z" fill="#ffffff"/>
    <path d="M0 879 L332 879 L286 950 L0 950 Z" fill="#f39a21"/>
    <path d="M597 0 L928 0 L928 1200 L560 1200 L560 820 C520 760 488 680 482 560 C476 380 520 170 597 0 Z" fill="url(#heroTone)" role="img" aria-label="Deep blue backdrop with a soft dove and foliage image"/>
    <path d="M600 580 C650 530 730 545 750 610 L765 700 C820 740 880 760 928 790 L928 1200 L470 1200 C510 1120 540 1060 552 990 C560 900 570 800 575 700 C580 640 585 600 600 580 Z" fill="url(#speakerTone)" role="img" aria-label="Photograph of the speaker seated in an orange suit"/>
  </svg>

  <div class="abs brand-name">HALVERN</div>

  <div class="theme-note">
    <span class="theme-pin"></span>
    <div class="theme-line first">IN FIRE</div>
    <div class="theme-band">AND</div>
    <div class="theme-line last">ON FIRE</div>
  </div>

  <h1>
    <span class="abs title-top">KESTREL</span>
    <span class="abs title-main">SUMMIT</span>
    <span class="abs title-year">2020</span>
  </h1>
  <p class="abs focus-words">Fire,&nbsp; Revival, Prophetic</p>

  <section class="session" style="left:55px; top:457px;">
    <div class="time-tag"><span class="time-hour">6</span><span class="time-min">:30</span><span class="time-pm">PM</span></div>
    <div class="session-day">Thursday</div>
    <div class="session-date">December 31st</div>
  </section>
  <section class="session" style="left:268px; top:457px;">
    <div class="time-tag"><span class="time-hour">6</span><span class="time-min">:30</span><span class="time-pm">PM</span></div>
    <div class="session-day">Friday</div>
    <div class="session-date">January 1st</div>
  </section>
  <section class="session" style="left:55px; top:611px;">
    <div class="time-tag"><span class="time-hour">6</span><span class="time-min">:30</span><span class="time-pm">PM</span></div>
    <div class="session-day">Saturday</div>
    <div class="session-date">January 2nd</div>
  </section>
  <section class="session" style="left:268px; top:611px;">
    <div class="time-tag"><span class="time-hour">4</span><span class="time-min">:30</span><span class="time-pm">PM</span></div>
    <div class="session-day">Sunday</div>
    <div class="session-date">January 3rd</div>
  </section>

  <p class="abs venue-name">Harlow Community Center</p>
  <p class="abs venue-address">239 Fennimore Street, Portland, ME 04117</p>

  <p class="abs speaker-label">SPEAKER:</p>
  <p class="abs speaker-name">Prophet Marcus Olunde</p>

  <p class="abs contact-heading">CONTACT INFORMATION:</p>
  <p class="abs contact-email">contact@brightmeadowfold.org</p>
  <p class="abs contact-line"><strong>207 583 2914 |</strong> www.<strong>halvern</strong>.org</p>
</main>
</body>
</html>
```